Webdesign for an Health & Beauty Center

We need a new modern and elegant web design for the relaunch of the http://veskarin.at/ website.
The website is for a company which offer all services for a beuty center like epilation, cosmetics and more.
The new website should use big emotional background images and a modern menu.
All in all the website should give a female expression and the design should be clear and not playful.
The existing logo used be used for the new design, the base colours of the existing website could be used optionally.

Reason: Review of the designs together with the customer needs a little more time.

Industry/Entity Type
It Company
Look and feel
Each slider illustrates characteristics of the customer's brand and the style your logo design should communicate.

```html
<!DOCTYPE html>
<html lang="de">
<head>
<meta charset="utf-8">
<title>Veskarin – Health &amp; Beauty center</title>
<link rel="stylesheet" href="https://fonts.googleapis.com/css2?family=Jura:wght@400;500;600;700&display=swap">
<style>
  :root {
    --olive: #8a9a24;
    --olive-dark: #56601a;
    --alert: #e0472a;
    --ink: #1c1c1c;
    --nav-bg: rgba(116, 96, 72, 0.72);
    --nav-active: #3a3026;
    --panel: #2e2e2e;
    --footer: #0b0b0b;
    --text-light: #f1f1f1;
    --muted: #9a9a9a;
  }
  * { box-sizing: border-box; margin: 0; padding: 0; }
  html, body { width: 1200px; height: 897px; overflow: hidden; }
  body { position: relative; font-family: "Jura", sans-serif; background: var(--footer); }

  .hero {
    position: absolute; left: 0; top: 0; width: 1200px; height: 515px;
    background:
      radial-gradient(ellipse 260px 200px at 1080px 90px, #f5dede 0%, rgba(245,222,222,0) 70%),
      radial-gradient(ellipse 230px 220px at 470px 400px, #f2b36d 0%, rgba(242,179,109,0) 70%),
      radial-gradient(ellipse 380px 260px at 560px 180px, #f3e2d0 0%, rgba(243,226,208,0) 75%),
      radial-gradient(ellipse 400px 300px at 150px 250px, #f6e6dc 0%, rgba(246,230,220,0) 75%),
      linear-gradient(180deg, #fbf8f3 0%, #f6efe3 60%, #efe2c7 100%);
  }

  .brand {
    position: absolute; left: 445px; top: 40px; width: 365px; text-align: center;
    font-weight: 600; font-size: 44px; color: var(--olive-dark); line-height: 1;
  }

  .tagline {
    position: absolute; left: 98px; top: 224px;
    font-weight: 600; font-size: 31px; color: var(--olive); letter-spacing: -0.6px; white-space: nowrap;
  }

  .contact {
    position: absolute; top: 235px; font-size: 16px; font-weight: 600; line-height: 22px; color: var(--ink); white-space: nowrap;
  }
  .contact.address { left: 746px; color: var(--olive-dark); }
  .contact.reach { left: 921px; }
  .contact .label { color: var(--alert); }

  .main-nav {
    position: absolute; left: 100px; top: 315px; width: 1000px; height: 59px;
    background: var(--nav-bg);
  }
  .main-nav a {
    position: absolute; top: 0; height: 59px; display: flex; align-items: center;
    color: #fff; text-decoration: none; font-weight: 700; font-size: 13px; letter-spacing: 0.6px; white-space: nowrap;
  }
  .main-nav a.is-active { left: 0; width: 86px; justify-content: center; background: var(--nav-active); }
  .main-nav .cart {
    position: absolute; left: 917px; top: 0; height: 59px; display: flex; align-items: center; gap: 12px;
    color: #fff; font-size: 20px;
  }

  .about {
    position: absolute; left: 0; top: 515px; width: 1200px; height: 325px;
    background:
      radial-gradient(ellipse 300px 200px at 60px 260px, rgba(120,60,110,0.35) 0%, rgba(120,60,110,0) 70%),
      radial-gradient(ellipse 500px 180px at 420px 40px, rgba(80,80,80,0.6) 0%, rgba(80,80,80,0) 70%),
      var(--panel);
    border-top: 4px solid var(--olive);
  }
  .about-notch { position: absolute; left: 583px; top: -14px; }

  .about h1 {
    position: absolute; left: 102px; top: 22px;
    font-weight: 600; font-size: 29px; color: #fff; letter-spacing: -0.3px;
  }
  .about .copy {
    position: absolute; left: 102px; top: 66px; width: 640px;
    font-size: 13.6px; line-height: 19px; color: var(--text-light); font-weight: 500;
  }
  .about .copy p + p { margin-top: 19px; }
  .divider { position: absolute; left: 770px; top: 58px; width: 1px; height: 216px; background: rgba(255,255,255,0.12); }

  .shop-card {
    position: absolute; left: 822px; top: 40px; width: 243px; height: 258px;
    border: 2px solid var(--olive); border-radius: 6px; overflow: hidden; background: var(--olive);
  }
  .shop-card .product-photo {
    height: 218px;
    background: linear-gradient(160deg, #c9c9c9 0%, #8d8f94 45%, #4a4c52 100%);
  }
  .shop-card .cta {
    display: block; height: 34px; line-height: 34px; text-align: center;
    color: #fff; font-weight: 700; font-size: 14px; letter-spacing: 0.6px; text-decoration: none;
  }

  .site-footer {
    position: absolute; left: 0; top: 840px; width: 1200px; height: 57px;
    background: var(--footer); border-top: 1px solid #222;
    text-align: center; font-size: 12px; color: var(--muted); padding-top: 18px;
  }
</style>
</head>
<body>
  <header class="hero" role="img" aria-label="Photo of a relaxed woman with flowers in her hair receiving a facial treatment, lilies on a towel in the corner">
    <div class="brand">Veskarin</div>
    <div class="tagline">Health &amp; Beauty center</div>
    <div class="contact address">Lindenweg 24-26<br>1100 Wien</div>
    <div class="contact reach"><span class="label">Tel. &amp; Fax:</span> 01/ 528 36 17<br><span class="label">E-Mail:</span> info veskarin.at</div>

    <nav class="main-nav">
      <a class="is-active" href="#">UBER UNS</a>
      <a href="#" style="left:110px">LEISTUNGEN</a>
      <a href="#" style="left:225px">GALERIE</a>
      <a href="#" style="left:313px">PFLEGELINIE</a>
      <a href="#" style="left:432px">ANGEBOTE</a>
      <a href="#" style="left:534px">PREISLISTEN</a>
      <a href="#" style="left:652px">KONTAKT</a>
      <span class="cart">
        <svg width="24" height="20" viewBox="0 0 24 20" aria-hidden="true">
          <path d="M1 2h4l3 11h12l3-8H7" fill="none" stroke="#fff" stroke-width="2" stroke-linejoin="round"/>
          <circle cx="10" cy="17" r="1.8" fill="#fff"/><circle cx="18" cy="17" r="1.8" fill="#fff"/>
        </svg>0
      </span>
    </nav>
  </header>

  <section class="about">
    <svg class="about-notch" width="24" height="12" viewBox="0 0 24 12" aria-hidden="true"><path d="M0 12L12 0L24 12Z" fill="var(--olive)"/></svg>
    <h1>Wer wir sind</h1>
    <div class="copy">
      <p>Veskarin die Nr. 1 für ästhetische Hautbehandlungen und dem führenden Anbieter von HighTech Ästhetik Geräten nach neuesten wissenschaftlichen Standards.</p>
      <p>Dabei legen wir nicht nur auf ein wirklich permanentes Ergebnis Wert, sondern auch auf schmerzfreie Behandlungen.</p>
      <p>Hautbehandlungen wie die Kavitaionstherapie und die Thermo Peel verjüngen die Haut ganz ohne OP und verleiht Ihnen ein frisches und jüngeres Aussehen, auch die Cryotherapie sorgt für ein feineres Hautbild. Überzeugen Sie sich selbst.</p>
      <p>Wir legen großen Wert auf Qualität und Sicherheit der eingesetzten medizinischen Geräte. Mit unseren starken Partnern können wir auf langjährige Erfahrung zurückgreifen.</p>
    </div>
    <div class="divider"></div>
    <div class="shop-card">
      <div class="product-photo" role="img" aria-label="Photo of skin care cream jar and lotion bottles on a slate surface"></div>
      <a class="cta" href="#">SHOP NOW</a>
    </div>
  </section>

  <footer class="site-footer">Impressum © 2014 Veskarin</footer>
</body>
</html>
```